Create Premium Wine Label Design

We are premium wine exporters from Australia. We are looking to introduce new brand " The Velloro" - in red wine, White wine and Sparkling wine to international market.

The sample label design for red wine ( Shiraz) is attached.

This is our luxury brand. We need a stunning wine label designs for (front, back and neck) that should be mostly in GOLD colour and design should be really eye catching.

We have provided sample design for front, back and neck labels. However, we are looking forward to see a completely new improvised design.

LOGO attached.

Front Label Design Specification:

* We would like to see designs that are in Gold colour.
* Wine Bottle size is standard: 750ml; we assume the same design can be resizable to different bottle sizes.
* Our design should suit both black, white and sparkling wine bottles(sample attached)
* Use our logo in the design (see attached - label sample)
* Content for front label (see attached).
* Design should include all information specified in the sample

Back Label Design
* All contents in the sample should be used ( sample attached)
* LOGO attached.

Neck Label Design
* Sample of Neck label attached, please provide similar or your own design.
* LOGO attached.

Image Samples:
* Samples of label designs we like (see attached)
* Sample for gold color (see attached)
* For bottle shapes (see attached)
* Front, Back and Neck Label Samples (see attached)

Target Market(s)

International Wine Market

Font styles to use
Decorative
Script

Requirements
Must have
• Must have golden color on front and back label

```html
<!DOCTYPE html>
<html lang="en">
<head>
<meta charset="utf-8">
<title>The Velloro Shiraz – Label Set</title>
<link href="https://fonts.googleapis.com/css2?family=Cinzel+Decorative:wght@700&family=Cinzel:wght@600;700&family=Fira+Sans+Condensed:wght@400;600&display=swap" rel="stylesheet">
<style>
  :root{
    --page:#ffffff;
    --gold:#c9a24a;
    --gold-light:#ecd58c;
    --gold-deep:#9a7424;
    --red-label:#121212;
    --white-label:#efeeea;
    --green-label:#0b2218;
    --ink-light:#f2f2f2;
    --ink-dark:#2a2a2a;
  }
  *{box-sizing:border-box;margin:0;padding:0}
  html,body{width:1200px;height:1200px;overflow:hidden;background:var(--page)}
  .canvas{position:relative;width:1200px;height:1200px}

  .label{position:absolute;overflow:hidden;background:var(--bg);color:var(--ink);text-align:center}
  .label--red{--bg:var(--red-label);--ink:var(--ink-light);--pattern:#5a5a5a;--mandala:#2c2c2c}
  .label--white{--bg:var(--white-label);--ink:var(--ink-dark);--pattern:#c9c9c9;--mandala:#dcdcdc}
  .label--sparkling{--bg:var(--green-label);--ink:var(--ink-light);--pattern:#8a6a22;--mandala:#3a3415}

  /* front labels */
  .front{width:190px;height:280px;top:250px}
  .front--red{left:115px}
  .front--white{left:536px}
  .front--sparkling{left:890px}
  .front__brand{margin-top:22px;font:700 14px/1 "Cinzel",serif;letter-spacing:1px;color:var(--gold)}
  .front__brand::before{content:"";display:block;width:14px;height:14px;margin:0 auto 8px;border-radius:50%;background:var(--gold)}
  .front__flourish{display:block;width:70px;height:8px;margin:6px auto 0;background:var(--gold-deep);opacity:.8;border-radius:4px}
  .front__mandala{position:absolute;left:35px;top:88px;width:120px;height:120px;border-radius:50%;background:radial-gradient(circle,var(--mandala) 40%,transparent 72%)}
  .front__body{position:relative;margin-top:30px}
  .varietal{font:700 30px/1 "Cinzel Decorative",serif;letter-spacing:3px;background:linear-gradient(180deg,var(--gold-light),var(--gold) 55%,var(--gold-deep));-webkit-background-clip:text;background-clip:text;color:transparent}
  .cuvee{margin-top:4px;font:700 14px/1 "Cinzel",serif;letter-spacing:2px;color:var(--gold)}
  .cuvee small{font-size:7px;letter-spacing:0;margin-right:3px;vertical-align:middle}
  .vintage{margin-top:14px;font:700 20px/1 "Cinzel",serif;color:var(--ink)}
  .origin-band{position:absolute;left:0;right:0;bottom:24px;height:18px;background:linear-gradient(90deg,var(--gold-deep),var(--gold-light) 50%,var(--gold-deep));font:700 10px/18px "Cinzel",serif;letter-spacing:.5px;color:#2a1c05}

  /* back labels */
  .back{width:186px;height:262px;top:806px}
  .back--red{left:118px}
  .back--white{left:539px}
  .back--sparkling{left:893px}
  .back__pattern{position:absolute;left:0;right:0;top:0;height:62px;background:linear-gradient(180deg,var(--pattern),transparent)}
  .back__title{position:relative;padding-top:24px}
  .back__title .varietal{font-size:28px}
  .back__copy{margin:12px 10px 0;font:400 5.2px/1.45 "Fira Sans Condensed",sans-serif;color:var(--ink)}
  .back__copy b{color:var(--gold);font-weight:600}
  .back__rule{width:46px;height:1px;margin:7px auto 4px;background:var(--gold)}
  .back__product{font:600 5px/1 "Fira Sans Condensed",sans-serif;color:var(--ink)}
  .back__facts{display:flex;justify-content:space-between;margin:6px 8px 0;font:400 4.6px/1.4 "Fira Sans Condensed",sans-serif;color:var(--ink);text-align:left}
  .back__facts div:last-child{text-align:right}
  .back__foot{position:absolute;left:0;right:0;bottom:12px;height:60px}
  .back__brand{position:absolute;left:62px;bottom:4px;font:700 12px/1 "Cinzel",serif;color:var(--gold)}
  .back__brand::before{content:"";display:block;width:12px;height:12px;margin:0 auto 8px;border-radius:50%;background:var(--gold)}
  .back__abv{position:absolute;right:22px;bottom:24px;font:600 4.5px/1 "Fira Sans Condensed",sans-serif;color:var(--ink);writing-mode:vertical-rl;transform:rotate(180deg)}
  .back__glass{position:absolute;right:6px;bottom:22px;width:14px;height:18px;background:#fff}
  .back__glass svg{display:block;width:14px;height:18px}
</style>
</head>
<body>
<main class="canvas">

  <!-- front labels -->
  <section class="label label--red front front--red" aria-label="Front label, red">
    <div class="front__brand">SOUTHVALE</div>
    <span class="front__flourish" role="img" aria-label="Gold ornamental flourish"></span>
    <div class="front__mandala" role="img" aria-label="Lace floral mandala pattern"></div>
    <div class="front__body">
      <div class="varietal">SHIRAZ</div>
      <div class="cuvee"><small>THE</small>VELLORO</div>
      <div class="vintage">2018</div>
    </div>
    <div class="origin-band">WINE OF AUSTRALIA</div>
  </section>

  <section class="label label--white front front--white" aria-label="Front label, white">
    <div class="front__brand">SOUTHVALE</div>
    <span class="front__flourish" role="img" aria-label="Gold ornamental flourish"></span>
    <div class="front__mandala" role="img" aria-label="Lace floral mandala pattern"></div>
    <div class="front__body">
      <div class="varietal">SHIRAZ</div>
      <div class="cuvee"><small>THE</small>VELLORO</div>
      <div class="vintage">2018</div>
    </div>
    <div class="origin-band">WINE OF AUSTRALIA</div>
  </section>

  <section class="label label--sparkling front front--sparkling" aria-label="Front label, sparkling">
    <div class="front__brand">SOUTHVALE</div>
    <span class="front__flourish" role="img" aria-label="Gold ornamental flourish"></span>
    <div class="front__mandala" role="img" aria-label="Gold lace floral mandala pattern"></div>
    <div class="front__body">
      <div class="varietal">SHIRAZ</div>
      <div class="cuvee"><small>THE</small>VELLORO</div>
      <div class="vintage">2018</div>
    </div>
    <div class="origin-band">WINE OF AUSTRALIA</div>
  </section>

  <!-- back labels -->
  <section class="label label--red back back--red" aria-label="Back label, red">
    <div class="back__pattern" role="img" aria-label="Lace floral border pattern"></div>
    <div class="back__title">
      <div class="varietal">SHIRAZ</div>
      <div class="cuvee"><small>THE</small>VELLORO</div>
    </div>
    <p class="back__copy"><b>Southvale Shiraz — the Velloro</b> is a classic fruit driven wine bursting with aromas of dark fruits and spice with background notes of charred French oak. This is a full bodied wine showcasing rich and juicy dark fruits of plum and cherry balanced with soft tannins and oak, providing a long lasting finish. This wine matches perfectly with range of rich and hearty red meat or pasta dishes.</p>
    <div class="back__rule"></div>
    <div class="back__product">Product of Australia</div>
    <div class="back__facts">
      <div>Preservative (220) Antioxidant (300)<br>May Contain Traces of Milk<br>Country of Origin : Australia</div>
      <div>Southvale Wines Pty. LTD.<br>Melbourne<br>Victoria, Australia</div>
    </div>
    <div class="back__foot">
      <div class="back__brand">SOUTHVALE</div>
      <div class="back__abv">12.5% Alc</div>
      <div class="back__glass"><svg viewBox="0 0 14 18"><path d="M4 3h6l-.5 4a2.5 2.5 0 0 1-5 0z" fill="#8a1020"/><path d="M7 9.5v5M5 14.5h4" stroke="#333" stroke-width=".8"/></svg></div>
    </div>
  </section>

  <section class="label label--white back back--white" aria-label="Back label, white">
    <div class="back__pattern" role="img" aria-label="Lace floral border pattern"></div>
    <div class="back__title">
      <div class="varietal">SHIRAZ</div>
      <div class="cuvee"><small>THE</small>VELLORO</div>
    </div>
    <p class="back__copy"><b>Southvale Shiraz — the Velloro</b> is a classic fruit driven wine bursting with aromas of dark fruits and spice with background notes of charred French oak. This is a full bodied wine showcasing rich and juicy dark fruits of plum and cherry balanced with soft tannins and oak, providing a long lasting finish. This wine matches perfectly with range of rich and hearty red meat or pasta dishes.</p>
    <div class="back__rule"></div>
    <div class="back__product">Product of Australia</div>
    <div class="back__facts">
      <div>Preservative (220) Antioxidant (300)<br>May Contain Traces of Milk<br>Country of Origin : Australia</div>
      <div>Southvale Wines Pty. LTD.<br>Melbourne<br>Victoria, Australia</div>
    </div>
    <div class="back__foot">
      <div class="back__brand">SOUTHVALE</div>
      <div class="back__abv">12.5% Alc</div>
      <div class="back__glass"><svg viewBox="0 0 14 18"><path d="M4 3h6l-.5 4a2.5 2.5 0 0 1-5 0z" fill="#8a1020"/><path d="M7 9.5v5M5 14.5h4" stroke="#333" stroke-width=".8"/></svg></div>
    </div>
  </section>

  <section class="label label--sparkling back back--sparkling" aria-label="Back label, sparkling">
    <div class="back__pattern" role="img" aria-label="Gold lace floral border pattern"></div>
    <div class="back__title">
      <div class="varietal">SHIRAZ</div>
      <div class="cuvee"><small>THE</small>VELLORO</div>
    </div>
    <p class="back__copy"><b>Southvale Shiraz — the Velloro</b> is a classic fruit driven wine bursting with aromas of dark fruits and spice with background notes of charred French oak. This is a full bodied wine showcasing rich and juicy dark fruits of plum and cherry balanced with soft tannins and oak, providing a long lasting finish. This wine matches perfectly with range of rich and hearty red meat or pasta dishes.</p>
    <div class="back__rule"></div>
    <div class="back__product">Product of Australia</div>
    <div class="back__facts">
      <div>Preservative (220) Antioxidant (300)<br>May Contain Traces of Milk<br>Country of Origin : Australia</div>
      <div>Southvale Wines Pty. LTD.<br>Melbourne<br>Victoria, Australia</div>
    </div>
    <div class="back__foot">
      <div class="back__brand">SOUTHVALE</div>
      <div class="back__abv">12.5% Alc</div>
      <div class="back__glass"><svg viewBox="0 0 14 18"><path d="M4 3h6l-.5 4a2.5 2.5 0 0 1-5 0z" fill="#8a1020"/><path d="M7 9.5v5M5 14.5h4" stroke="#333" stroke-width=".8"/></svg></div>
    </div>
  </section>

</main>
</body>
</html>
```